Dalvor Inc Business Card

Looking to get an updated business card for a Contract Machining company (www.dalvorinc-example.com) - looking for a clean design the portrays the technical nature of the business - colors can follow the website design and be in any combination that makes sense (red black, white, metallic or silver) - logos attached for use also. Would like space for: Name, title, business phone (555 214-3098), cell phone , website (www.dalvorinc-example.com) - possibly QR code could be integrated for website (designer choice), business address - 418 Birchfield Lane, Brennick, MI 49107 (cards will be for 4 employees, I will either need to modify a template or I can provide individual information)
Target Market(s)
Aerospace, defense and medical device manufacturing companies that need machining
Industry/Entity Type
Machining for aerospace, defense, medical
Contact Information for Business Card
Name, Title, Business Phone, Cell Phone, email, business website and business address

```html
<!DOCTYPE html>
<html lang="en">
<head>
<meta charset="utf-8">
<title>Dalvor Inc Business Card</title>
<link rel="stylesheet" href="https://fonts.googleapis.com/css2?family=Poppins:wght@400;700;800&display=swap">
<style>
  :root {
    --brand-red: #b01e23;
    --ink: #1a1a1a;
    --paper: #ffffff;
    --rule: #9a9a9a;
    --back-dark: #0e0f10;
    --back-mid: #2a2c2e;
    --stage: #e6e6e6;
  }
  * { box-sizing: border-box; margin: 0; padding: 0; }
  html, body { width: 1200px; height: 1108px; overflow: hidden; }
  body {
    background: var(--stage);
    font-family: "Poppins", sans-serif;
    color: var(--ink);
    position: relative;
  }
  .card {
    position: absolute;
    top: 214px;
    width: 400px;
    height: 680px;
    border-radius: 26px;
    overflow: hidden;
    box-shadow: 0 10px 30px rgba(0,0,0,0.18);
  }
  .card-front {
    left: 170px;
    background: var(--paper);
    display: flex;
    flex-direction: column;
    align-items: center;
    padding-top: 44px;
    text-align: center;
  }
  .card-back { left: 630px; background: var(--back-dark); }

  .brand-disc {
    width: 210px; height: 210px; border-radius: 50%;
    background: var(--brand-red);
    flex-shrink: 0;
  }
  .brand-name {
    margin-top: 14px;
    color: var(--brand-red);
    font-weight: 800;
    font-size: 42px;
    letter-spacing: 1px;
    line-height: 1.05;
  }
  .person-name {
    margin-top: 28px;
    color: var(--brand-red);
    font-weight: 700;
    font-size: 23px;
    letter-spacing: 0.5px;
    line-height: 1.4;
    text-transform: uppercase;
  }
  .person-title { font-size: 18px; font-weight: 400; line-height: 1.4; }

  .icon-row {
    margin-top: 14px;
    display: flex; align-items: center; gap: 6px;
    width: 300px;
  }
  .icon-row .rule { flex: 1; height: 1px; background: var(--rule); }
  .contact-icon {
    width: 30px; height: 30px; border-radius: 5px;
    background: var(--brand-red);
    display: flex; align-items: center; justify-content: center;
  }
  .contact-list {
    margin-top: 10px;
    font-size: 17px; line-height: 1.45; list-style: none;
  }
  .contact-list .accent { color: var(--brand-red); }
  .divider { width: 300px; height: 1px; background: var(--rule); margin-top: 8px; }
  .address { margin-top: 8px; font-size: 17px; line-height: 1.45; font-style: normal; }

  .back-surface {
    position: absolute; inset: 0;
    background: linear-gradient(215deg, var(--back-mid) 0%, #1a1b1d 45%, var(--back-dark) 100%);
  }
  .back-disc {
    position: absolute; left: 196px; top: 498px;
    width: 44px; height: 44px; border-radius: 50%;
    background: var(--brand-red);
  }
</style>
</head>
<body>
  <section class="card card-front" aria-label="Business card front">
    <div class="brand-disc"></div>
    <div class="brand-name">DALVOR INC</div>

    <h1 class="person-name">Marcus Hale</h1>
    <p class="person-title">Managing Director</p>

    <div class="icon-row">
      <span class="rule"></span>
      <span class="contact-icon" aria-label="Phone">
        <svg width="18" height="18" viewBox="0 0 24 24" fill="#fff"><path d="M6.6 10.8a15 15 0 0 0 6.6 6.6l2.2-2.2a1 1 0 0 1 1-.25 11.4 11.4 0 0 0 3.6.57 1 1 0 0 1 1 1V20a1 1 0 0 1-1 1A17 17 0 0 1 3 4a1 1 0 0 1 1-1h3.5a1 1 0 0 1 1 1c0 1.25.2 2.45.57 3.57a1 1 0 0 1-.25 1z"/></svg>
      </span>
      <span class="contact-icon" aria-label="Mobile">
        <svg width="18" height="18" viewBox="0 0 24 24" fill="none" stroke="#fff" stroke-width="2"><rect x="7" y="2" width="10" height="20" rx="2"/><line x1="11" y1="18" x2="13" y2="18"/></svg>
      </span>
      <span class="contact-icon" aria-label="Email">
        <svg width="18" height="18" viewBox="0 0 24 24" fill="none" stroke="#fff" stroke-width="2"><rect x="3" y="5" width="18" height="14"/><path d="M3 5l9 8 9-8"/></svg>
      </span>
      <span class="contact-icon" aria-label="Website">
        <svg width="18" height="18" viewBox="0 0 24 24" fill="none" stroke="#fff" stroke-width="2"><circle cx="12" cy="12" r="9"/><path d="M3 12h18M12 3c3 3 3 15 0 18M12 3c-3 3-3 15 0 18"/></svg>
      </span>
      <span class="rule"></span>
    </div>

    <ul class="contact-list">
      <li>555 214-3098</li>
      <li>044-555 018 273</li>
      <li>info@dalvorinc-example.com</li>
      <li>www.<span class="accent">dalvorinc-example</span>.com</li>
    </ul>
    <div class="divider"></div>
    <address class="address">418 Birchfield Lane,<br>Brennick, MI 49107</address>
  </section>

  <section class="card card-back" aria-label="Business card back">
    <div class="back-surface" role="img" aria-label="Repeating pattern of brand emblems in gloss black fading to silver"></div>
    <div class="back-disc"></div>
  </section>
</body>
</html>
```